Business Card Design Project

Hello Designers, hope you are all aiming enjoy the weekend
I have the Business Logo (uploaded), you can alter the color which ever way you think would work,
Im looking for a simple yet striking feel, something which will stay memorable (I have uploaded 3 examples for you to flick through)
Information on the card, will just be the bare minimum,
Double Sided
Info being
i.e.
Name
Number
Website
ABN
Tobin Wexmoor
+468213579 (singapore)
+315792846 (Australia)
+729384615 (America)
www.lomevu-linkup.example
ABN 86420913
Enjoy,
Tobin
Industry/Entity Type
Business
Look and feel
Each slider illustrates characteristics of the customer's brand and the style your logo design should communicate.

```html
<!DOCTYPE html>
<html lang="en">
<head>
<meta charset="utf-8">
<title>Lomevu Linkup – Business Card</title>
<link rel="stylesheet" href="https://fonts.googleapis.com/css2?family=Noto+Serif:wght@400;700&display=swap">
<style>
  :root {
    --backdrop: #d9d9d9;
    --card-dark: #2f2f2f;
    --card-mid: #3d3d3d;
    --card-light: #5a5a5a;
    --accent-pink: #ee5c8f;
    --brand-white: #f4f4f4;
    --panel-white: #ffffff;
    --ink: #141414;
  }
  * { margin: 0; padding: 0; box-sizing: border-box; }
  html, body {
    width: 1200px;
    height: 868px;
    overflow: hidden;
    background: var(--backdrop);
  }
  .canvas {
    position: relative;
    width: 1200px;
    height: 868px;
    font-family: "Noto Serif", Georgia, serif;
  }
  .card {
    position: absolute;
    width: 688px;
    height: 382px;
    border-radius: 40px;
    background: radial-gradient(ellipse at 45% 20%, var(--card-mid) 0%, var(--card-dark) 75%);
  }
  .card--front { left: 110px; top: 40px; }
  .card--back {
    left: 397px; top: 447px;
    background: radial-gradient(ellipse at 15% 10%, var(--card-light) 0%, var(--card-mid) 35%, var(--card-dark) 85%);
  }
  .brand {
    position: absolute;
    display: flex;
    align-items: center;
    gap: 16px;
  }
  .brand__mark {
    width: 40px;
    height: 40px;
    border-radius: 50%;
    background: var(--accent-pink);
  }
  .brand__name {
    font-size: 42px;
    font-weight: 400;
    color: var(--brand-white);
    letter-spacing: 0.5px;
    line-height: 1;
  }
  .card--front .brand { left: 228px; top: 292px; }
  .card--back .brand { left: 28px; top: 44px; }
  .contact-panel {
    position: absolute;
    left: 14px;
    top: 125px;
    width: 383px;
    height: 240px;
    border-radius: 24px;
    background: var(--panel-white);
    padding: 26px 28px 0 30px;
    color: var(--ink);
  }
  .contact-panel__name {
    font-size: 25px;
    font-weight: 700;
    margin-left: 12px;
    margin-bottom: 12px;
    line-height: 1.2;
  }
  .contact-panel__list { list-style: none; }
  .contact-panel__list li {
    font-size: 21px;
    line-height: 29px;
    white-space: nowrap;
  }
</style>
</head>
<body>
  <main class="canvas">
    <section class="card card--front" aria-label="Card front">
      <div class="brand">
        <span class="brand__mark"></span>
        <span class="brand__name">Lomevu Linkup</span>
      </div>
    </section>

    <section class="card card--back" aria-label="Card back">
      <div class="brand">
        <span class="brand__mark"></span>
        <span class="brand__name">Lomevu Linkup</span>
      </div>
      <div class="contact-panel">
        <p class="contact-panel__name">Tobin Wexmoor</p>
        <ul class="contact-panel__list">
          <li>+468213579 (singapore)</li>
          <li>+315792846 (Australia)</li>
          <li>+729384615 (America)</li>
          <li>www.lomevu-linkup.example</li>
          <li>ABN 86420913</li>
        </ul>
      </div>
    </section>
  </main>
</body>
</html>
```